Simple and Clean business card design

We would like the design to be simple clean and to incorporate our colors.

We are open to your design and talent, we have the dots in our logo as we think of it as data points and we connect data points for people.

We are open to see the great creative and clean design you bring to the table

Contact Information for Business Card

please include: name, position, email, phone and website

Font styles to use
Sans Serif

Requirements
Must have
• my colors incorporated, simplicity
Nice to have
• lots of white space, simplicity
Should not have
• complexicity/ complex art

```html
<!DOCTYPE html>
<html lang="en">
<head>
<meta charset="utf-8">
<title>Nodera Business Card</title>
<link rel="stylesheet" href="https://fonts.googleapis.com/css2?family=Montserrat:wght@400;500;600&display=swap">
<style>
  :root {
    --bg: #e4e4e4;
    --paper: #f7f7f7;
    --blue: #2f66de;
    --blue-light: #5a8ee8;
    --green: #2f9a4e;
    --yellow: #f1b700;
    --red: #e0463a;
    --ink: #111111;
    --muted: #555555;
    --accent-text: #4f7ee0;
  }
  * { margin: 0; padding: 0; box-sizing: border-box; }
  html, body { width: 1200px; height: 1200px; overflow: hidden; }
  body {
    background: var(--bg);
    font-family: "Montserrat", sans-serif;
    position: relative;
  }
  .card {
    position: absolute;
    left: 257px;
    width: 686px;
    height: 392px;
    border-radius: 20px;
    overflow: hidden;
  }
  .card--front { top: 160px; background: var(--paper); }
  .card--back {
    top: 648px;
    background: linear-gradient(225deg, var(--blue-light) 0%, var(--blue) 55%, #2b5fd6 100%);
  }
  .colour-band {
    position: absolute;
    left: 0;
    bottom: 0;
    width: 100%;
    height: 14px;
    display: flex;
  }
  .colour-band__segment { flex: 1; }
  .colour-band__segment--blue { background: var(--blue); }
  .colour-band__segment--green { background: var(--green); }
  .colour-band__segment--yellow { background: var(--yellow); }
  .colour-band__segment--red { background: var(--red); }
  .card--back .colour-band__segment--blue { background: #ffffff; }
  .identity {
    position: absolute;
    right: 69px;
    top: 196px;
    text-align: right;
  }
  .identity__name {
    font-size: 24px;
    font-weight: 600;
    color: var(--ink);
    letter-spacing: 0.5px;
    line-height: 1;
  }
  .identity__role {
    font-size: 16px;
    font-weight: 400;
    color: var(--accent-text);
    margin-top: 6px;
    line-height: 1;
    letter-spacing: 0.3px;
  }
  .identity__rule {
    width: 63px;
    height: 1.5px;
    background: var(--ink);
    margin: 17px 0 0 auto;
  }
  .contacts {
    position: absolute;
    right: 69px;
    top: 280px;
    list-style: none;
  }
  .contacts__item {
    display: flex;
    justify-content: flex-end;
    align-items: center;
    gap: 9px;
    height: 21px;
    font-size: 16px;
    color: var(--muted);
    letter-spacing: 0.2px;
  }
  .contacts__icon { width: 17px; height: 17px; flex: none; }
  .wordmark {
    position: absolute;
    right: 69px;
    top: 252px;
    font-size: 84px;
    font-weight: 600;
    color: var(--ink);
    line-height: 1;
    letter-spacing: -1px;
  }
</style>
</head>
<body>

<section class="card card--front">
  <div class="identity">
    <div class="identity__name">JORDAN HALE</div>
    <div class="identity__role">President</div>
    <div class="identity__rule"></div>
  </div>

  <ul class="contacts">
    <li class="contacts__item">555-204-7318
      <svg class="contacts__icon" viewBox="0 0 20 20" aria-hidden="true">
        <circle cx="10" cy="10" r="10" fill="var(--green)"/>
        <path d="M7 5.5c.6-.4 1.1-.2 1.4.4l.7 1.4c.2.5.1.9-.3 1.2l-.6.5c.5 1.1 1.5 2.1 2.6 2.6l.5-.6c.3-.4.7-.5 1.2-.3l1.4.7c.6.3.8.8.4 1.4-.6 1-1.6 1.4-2.7 1-2.6-.9-4.6-2.9-5.5-5.5-.4-1.1 0-2.1.9-2.8z" fill="#fff"/>
      </svg>
    </li>
    <li class="contacts__item">hello@nodera.co
      <svg class="contacts__icon" viewBox="0 0 20 20" aria-hidden="true">
        <circle cx="10" cy="10" r="10" fill="var(--yellow)"/>
        <rect x="5" y="6.5" width="10" height="7" rx="1" fill="#fff"/>
        <path d="M5.5 7.2l4.5 3.4 4.5-3.4" fill="none" stroke="var(--yellow)" stroke-width="1"/>
      </svg>
    </li>
    <li class="contacts__item">nodera.co
      <svg class="contacts__icon" viewBox="0 0 20 20" aria-hidden="true">
        <circle cx="10" cy="10" r="10" fill="var(--red)"/>
        <circle cx="10" cy="10" r="5" fill="none" stroke="#fff" stroke-width="1.4"/>
        <path d="M5 10h10M10 5c-2 2.8-2 7.2 0 10M10 5c2 2.8 2 7.2 0 10" fill="none" stroke="#fff" stroke-width="1.1"/>
      </svg>
    </li>
  </ul>

  <div class="colour-band" aria-hidden="true">
    <span class="colour-band__segment colour-band__segment--blue"></span>
    <span class="colour-band__segment colour-band__segment--green"></span>
    <span class="colour-band__segment colour-band__segment--yellow"></span>
    <span class="colour-band__segment colour-band__segment--red"></span>
  </div>
</section>

<section class="card card--back">
  <div class="wordmark">Nodera</div>
  <div class="colour-band" aria-hidden="true">
    <span class="colour-band__segment colour-band__segment--blue"></span>
    <span class="colour-band__segment colour-band__segment--green"></span>
    <span class="colour-band__segment colour-band__segment--yellow"></span>
    <span class="colour-band__segment colour-band__segment--red"></span>
  </div>
</section>

</body>
</html>
```